Electrical company business card design.

Hi, were an electrical company in Auckland New Zealand called Quarneth Ltd. We focus mainly on high end residential and commercial so the card would be targeted towards that.
The card will be for myself, i am the director of the company.
Name: Derek Olstow
Position: Director/electrician
Phone: 021 387 9415
Email: derek@quarneth.co.nz
Location: Auckland
As for colors the the blue color in the logo is preferred, i also don't mind a black background option.
Target Market(s)
High end residential and commercial
Industry/Entity Type
Electrician
Contact Information for Business Card
Name: Derek Olstow Position: Director/Electrician Phone: 021 387 9415, Email: derek@quarneth.co.nz, Location: Auckland

```html
<!DOCTYPE html>
<html lang="en">
<head>
<meta charset="utf-8">
<title>Quarneth Ltd – Business Card</title>
<link rel="stylesheet" href="https://fonts.googleapis.com/css2?family=Michroma&display=swap">
<style>
  :root {
    --stage: #2b2b2d;
    --card-dark: #1c1c1e;
    --card-light: #ffffff;
    --brand-blue: #1273c9;
    --brand-grey: #4a4e52;
    --tagline-grey: #55595d;
    --text-grey: #45494d;
  }
  * { margin: 0; padding: 0; box-sizing: border-box; }
  html, body {
    width: 1200px; height: 689px; overflow: hidden;
    background: var(--stage);
    font-family: "Michroma", sans-serif;
  }
  .canvas {
    position: relative; width: 1200px; height: 689px;
    display: flex; align-items: center; justify-content: center; gap: 50px;
  }
  .card {
    position: relative; width: 520px; height: 300px;
    border-radius: 22px; overflow: hidden;
  }
  .card--back {
    background: var(--card-dark);
    display: flex; flex-direction: column; align-items: center; justify-content: center;
  }
  .card--back .wordmark { font-size: 50px; color: var(--brand-grey); letter-spacing: 2px; white-space: nowrap; }
  .card--back .tagline { margin-top: 12px; font-size: 15px; color: var(--tagline-grey); letter-spacing: 3px; white-space: nowrap; }

  .card--front { background: var(--card-light); }
  .front-brand { position: absolute; left: 44px; top: 34px; }
  .front-brand .wordmark { font-size: 30px; color: var(--brand-grey); letter-spacing: 1px; white-space: nowrap; }
  .front-brand .tagline { margin-top: 6px; font-size: 9px; color: var(--tagline-grey); letter-spacing: 1.5px; white-space: nowrap; }

  .person { position: absolute; left: 44px; top: 134px; }
  .person .name { font-size: 22px; color: var(--text-grey); letter-spacing: 1px; white-space: nowrap; }
  .person .name .first { color: var(--brand-blue); }
  .person .role { margin-top: 6px; font-size: 11px; color: var(--text-grey); letter-spacing: 1px; white-space: nowrap; }

  .contact { position: absolute; left: 44px; top: 212px; list-style: none; }
  .contact li { display: flex; align-items: center; gap: 12px; color: var(--text-grey); white-space: nowrap; }
  .contact .phone { font-size: 18px; }
  .contact .location { font-size: 13px; margin-top: 8px; }
  .contact svg { width: 16px; height: 16px; fill: var(--brand-blue); flex: none; }

  .edge-tab { position: absolute; left: 0; width: 20px; height: 34px; background: var(--brand-blue); }
  .edge-tab--upper { top: 150px; }
  .edge-tab--lower { top: 232px; }
</style>
</head>
<body>
<main class="canvas">
  <section class="card card--back" aria-label="Card back">
    <div class="wordmark">QUARNETH</div>
    <div class="tagline">CURRENT DONE RIGHT</div>
  </section>

  <section class="card card--front" aria-label="Card front">
    <div class="front-brand">
      <div class="wordmark">QUARNETH</div>
      <div class="tagline">CURRENT DONE RIGHT</div>
    </div>

    <span class="edge-tab edge-tab--upper"></span>
    <span class="edge-tab edge-tab--lower"></span>

    <div class="person">
      <div class="name"><span class="first">DEREK</span> OLSTOW</div>
      <div class="role">DIRECTOR/ELECTRICIAN</div>
    </div>

    <ul class="contact">
      <li class="phone">
        <svg viewBox="0 0 24 24" aria-hidden="true"><path d="M6.6 10.8a15.1 15.1 0 0 0 6.6 6.6l2.2-2.2a1 1 0 0 1 1-.25 11.4 11.4 0 0 0 3.6.57 1 1 0 0 1 1 1V20a1 1 0 0 1-1 1A17 17 0 0 1 3 4a1 1 0 0 1 1-1h3.5a1 1 0 0 1 1 1c0 1.25.2 2.45.57 3.57a1 1 0 0 1-.25 1z"/></svg>
        021 387 9415
      </li>
      <li class="location">
        <svg viewBox="0 0 24 24" aria-hidden="true"><path d="M12 2a7 7 0 0 0-7 7c0 5.25 7 13 7 13s7-7.75 7-13a7 7 0 0 0-7-7zm0 9.5A2.5 2.5 0 1 1 12 6.5a2.5 2.5 0 0 1 0 5z"/></svg>
        Auckland
      </li>
    </ul>
  </section>
</main>
</body>
</html>
```